Real estate development company, seeking investors and joint venture partners to fund

i have attached a investor proposal document to attact joint venture money partners to invest in property development. the existing document i have attached need s to be polised to a professional standard and needs to be in word , so i can edit the content on ongoing basis i.e. numbers and photos etc . this document will be updated with new opportunites, propoerties, feasibility edited and emailed to potential investors. This document needs to be Red hot!! Company name Bright meadow collective. All tables, place holders for photos need to be provided so i can easily remove and paste new /updated photos.

Target Market(s)

investors , money partners property developers

Requirements
Must have
• Design to be in word document

Content should be modifyable by me as each project will have unique cost, sales etc

i want to be able to email to my clients

i may also print as required
Nice to have
• Feel free to modify table/images/look and feel

```html
<!DOCTYPE html>
<html lang="en">
<head>
<meta charset="utf-8">
<title>Bright Meadow Collective – Investor Proposal</title>
<link href="https://fonts.googleapis.com/css2?family=Oswald:wght@500;600;700&family=Montserrat:ital,wght@0,300;0,400;0,600;0,700;0,800;1,400;1,600&display=swap" rel="stylesheet">
<style>
  :root {
    --orange: #c9671a;
    --orange-soft: #e0914f;
    --ink: #262626;
    --grey: #4a4a4a;
    --paper: #ffffff;
    --stage: #e4dad4;
    --night-1: #14233f;
    --night-2: #2c5f95;
  }
  * { box-sizing: border-box; margin: 0; padding: 0; }
  html, body { width: 1200px; height: 2400px; overflow: hidden; }
  body {
    background: var(--stage);
    font-family: "Montserrat", Arial, sans-serif;
    color: var(--ink);
    position: relative;
  }
  .page {
    position: absolute;
    width: 520px;
    height: 735px;
    background: var(--paper);
    overflow: hidden;
    box-shadow: 0 10px 30px rgba(60, 40, 30, 0.18);
  }
  .page .shapes { position: absolute; inset: 0; width: 100%; height: 100%; }
  .abs { position: absolute; }

  /* positions */
  .cover--solo { left: 340px; top: 40px; }
  .back-cover { left: 80px; top: 830px; }
  .cover--spread { left: 600px; top: 830px; }
  .contents-page { left: 80px; top: 1625px; }
  .proposal-page { left: 600px; top: 1625px; }

  /* front cover */
  .brand-title {
    font-family: "Oswald", "Arial Narrow", sans-serif;
    font-weight: 600;
    color: var(--paper);
    font-size: 32px;
    letter-spacing: 1px;
    left: 0; right: 0; top: 22px;
    text-align: center;
  }
  .cover-tagline { left: 0; right: 0; top: 596px; text-align: center; }
  .tagline-lead {
    color: var(--orange);
    font-weight: 800;
    font-size: 19px;
    letter-spacing: 0.5px;
    line-height: 1.15;
  }
  .tagline-rest {
    font-weight: 600;
    font-size: 15px;
    letter-spacing: 0.8px;
    line-height: 1.25;
    color: var(--ink);
  }
  .rule {
    width: 84px; height: 3px; background: var(--orange);
    margin: 10px auto 0;
  }
  .web {
    font-size: 11px;
    font-weight: 600;
    color: var(--ink);
  }
  .web span { color: var(--orange); }
  .cover-web { left: 0; right: 0; top: 690px; text-align: center; }

  /* back cover */
  .thanks { left: 40px; top: 490px; color: var(--paper); }
  .thanks-bold { font-weight: 800; font-size: 27px; letter-spacing: 1px; line-height: 1.1; }
  .thanks-light { font-weight: 300; font-size: 24px; letter-spacing: 1.5px; line-height: 1.1; }
  .back-name {
    font-family: "Oswald", "Arial Narrow", sans-serif;
    font-weight: 600; font-size: 21px; color: var(--ink);
    left: 150px; top: 630px;
  }
  .contact-list { left: 250px; top: 672px; list-style: none; }
  .contact-list li {
    display: flex; align-items: center; gap: 7px;
    font-size: 10px; color: var(--ink); margin-bottom: 6px;
  }
  .contact-list svg { width: 11px; height: 11px; flex: none; }
  .call { left: 36px; top: 672px; }
  .call-label { color: var(--orange); font-size: 12px; font-weight: 600; letter-spacing: 0.5px; }
  .call-number { font-size: 21px; font-weight: 700; letter-spacing: 1px; color: var(--ink); }

  /* contents */
  .contents-mark { left: 36px; top: 62px; width: 44px; height: 34px; background: var(--orange); }
  .contents-title {
    font-family: "Oswald", "Arial Narrow", sans-serif;
    font-weight: 700; font-style: italic;
    font-size: 42px; letter-spacing: 1px; color: var(--ink);
    left: 98px; top: 46px;
  }
  .toc { left: 60px; right: 56px; top: 140px; list-style: none; }
  .toc li {
    display: flex; align-items: baseline;
    height: 38px;
    font-style: italic; font-size: 12px; color: var(--ink);
  }
  .toc .leader { flex: 1; border-bottom: 1px dotted #8a8a8a; margin: 0 8px; transform: translateY(-3px); }
  .toc .num { color: var(--orange); font-weight: 700; font-style: normal; font-size: 17px; width: 24px; text-align: right; }
  .contents-web { left: 60px; top: 630px; }

  /* proposal */
  .proposal-band { left: 24px; top: 0; width: 58px; height: 100%; background: var(--orange); }
  .proposal-title {
    font-family: "Oswald", "Arial Narrow", sans-serif;
    font-weight: 600; font-size: 42px; letter-spacing: 1.5px; color: #3a3a3a;
    left: 118px; top: 46px;
  }
  .proposal-photo {
    left: 52px; top: 128px; width: 428px; height: 228px;
    border: 4px solid var(--paper);
    background: linear-gradient(135deg, #d9dde2 0%, #b9c0c8 45%, #e9e7e3 100%);
    box-shadow: 0 2px 6px rgba(0,0,0,0.15);
  }
  .proposal-body { left: 112px; right: 40px; top: 382px; }
  .section-head { color: var(--orange); font-weight: 700; font-size: 15px; margin-bottom: 6px; }
  .body-copy { font-size: 10px; line-height: 1.45; color: var(--grey); margin-bottom: 22px; }
  .outcomes { list-style: none; font-size: 10px; line-height: 1.6; color: var(--grey); }
  .proposal-web { left: 112px; top: 660px; }
</style>
</head>
<body>

<!-- Front cover -->
<section class="page cover cover--solo">
  <svg class="shapes" viewBox="0 0 520 735" aria-hidden="false">
    <defs>
      <linearGradient id="night-a" x1="0" y1="0" x2="0" y2="1">
        <stop offset="0" stop-color="#14233f"/>
        <stop offset="1" stop-color="#2c5f95"/>
      </linearGradient>
    </defs>
    <rect x="0" y="0" width="520" height="92" fill="#c9671a"/>
    <polygon points="470,92 520,92 520,455 470,467" fill="#c9671a"/>
    <polygon role="img" aria-label="Photo of a hand holding a tablet with a lit city skyline and connected network icons against a starry night sky" points="30,108 470,108 470,467 30,568" fill="url(#night-a)" stroke="#ffffff" stroke-width="3"/>
  </svg>
  <h1 class="abs brand-title">BRIGHT MEADOW COLLECTIVE</h1>
  <div class="abs cover-tagline">
    <p class="tagline-lead">REAL ESTATE DEVELOPMENT AND</p>
    <p class="tagline-rest">HOLDING COMPANY SPECIALIZING IN<br>AFFORDABLE HOUSING</p>
    <div class="rule"></div>
  </div>
  <p class="abs web cover-web">www.<span>brightmeadowcollective</span>.com</p>
</section>

<!-- Back cover -->
<section class="page back-cover">
  <svg class="shapes" viewBox="0 0 520 735">
    <defs>
      <linearGradient id="amber" x1="0" y1="0" x2="1" y2="1">
        <stop offset="0" stop-color="#e39a5a"/>
        <stop offset="0.6" stop-color="#d47a32"/>
        <stop offset="1" stop-color="#c9671a"/>
      </linearGradient>
    </defs>
    <polygon role="img" aria-label="Orange-tinted photo of a curving city roadway at dusk" points="0,0 520,0 520,540 0,640" fill="url(#amber)"/>
  </svg>
  <div class="abs thanks">
    <p class="thanks-bold">THANK YOU FOR</p>
    <p class="thanks-light">YOUR BUSINESS</p>
  </div>
  <p class="abs back-name">BRIGHT MEADOW COLLECTIVE</p>
  <ul class="abs contact-list">
    <li>
      <svg viewBox="0 0 12 12"><rect x="1" y="2.5" width="10" height="7" fill="none" stroke="#c9671a" stroke-width="1.2"/><polyline points="1,2.5 6,6.5 11,2.5" fill="none" stroke="#c9671a" stroke-width="1.2"/></svg>
      info@brightmeadowcollective.com.au
    </li>
    <li>
      <svg viewBox="0 0 12 12"><circle cx="6" cy="6" r="5" fill="none" stroke="#c9671a" stroke-width="1.2"/><ellipse cx="6" cy="6" rx="2.2" ry="5" fill="none" stroke="#c9671a" stroke-width="1"/><line x1="1" y1="6" x2="11" y2="6" stroke="#c9671a" stroke-width="1"/></svg>
      www.brightmeadowcollective.com.au
    </li>
  </ul>
  <div class="abs call">
    <p class="call-label">CALL US NOW</p>
    <p class="call-number">0400-555-218</p>
  </div>
</section>

<!-- Front cover in spread -->
<section class="page cover cover--spread">
  <svg class="shapes" viewBox="0 0 520 735">
    <defs>
      <linearGradient id="night-b" x1="0" y1="0" x2="0" y2="1">
        <stop offset="0" stop-color="#14233f"/>
        <stop offset="1" stop-color="#2c5f95"/>
      </linearGradient>
    </defs>
    <rect x="0" y="0" width="520" height="92" fill="#c9671a"/>
    <polygon points="470,92 520,92 520,455 470,467" fill="#c9671a"/>
    <polygon role="img" aria-label="Photo of a hand holding a tablet with a lit city skyline and connected network icons against a starry night sky" points="30,108 470,108 470,467 30,568" fill="url(#night-b)" stroke="#ffffff" stroke-width="3"/>
  </svg>
  <h1 class="abs brand-title">BRIGHT MEADOW COLLECTIVE</h1>
  <div class="abs cover-tagline">
    <p class="tagline-lead">REAL ESTATE DEVELOPMENT AND</p>
    <p class="tagline-rest">HOLDING COMPANY SPECIALIZING IN<br>AFFORDABLE HOUSING</p>
    <div class="rule"></div>
  </div>
  <p class="abs web cover-web">www.<span>brightmeadowcollective</span>.com</p>
</section>

<!-- Contents -->
<section class="page contents-page">
  <div class="abs contents-mark"></div>
  <h2 class="abs contents-title">CONTENTS</h2>
  <ol class="abs toc">
    <li>Proposal<span class="leader"></span><span class="num">4</span></li>
    <li>Location<span class="leader"></span><span class="num">4</span></li>
    <li>Photos<span class="leader"></span><span class="num">5</span></li>
    <li>Financial Feasibility<span class="leader"></span><span class="num">5</span></li>
    <li>Cash Flow Analysis<span class="leader"></span><span class="num">6</span></li>
    <li>Capital Requirements<span class="leader"></span><span class="num">7</span></li>
    <li>Suburb Profile<span class="leader"></span><span class="num">8</span></li>
    <li>Comparable Sales Data<span class="leader"></span><span class="num">10</span></li>
    <li>Planning Information<span class="leader"></span><span class="num">13</span></li>
    <li>Testimonials<span class="leader"></span><span class="num">16</span></li>
    <li>Who Are You?<span class="leader"></span><span class="num">16</span></li>
    <li>Contact<span class="leader"></span><span class="num">20</span></li>
  </ol>
  <p class="abs web contents-web">www.<span>brightmeadowcollective</span>.com</p>
</section>

<!-- Proposal -->
<section class="page proposal-page">
  <div class="abs proposal-band"></div>
  <h2 class="abs proposal-title">PROPOSAL</h2>
  <div class="abs proposal-photo" role="img" aria-label="Photo of hands working on a laptop over architectural floor plans"></div>
  <div class="abs proposal-body">
    <h3 class="section-head">Project Goal</h3>
    <p class="body-copy">Purchase an existing house on a block of land, obtain development approval to demolish existing house and build two townhouses (dual occupancy side by side)</p>
    <h3 class="section-head">Project Outcomes</h3>
    <ul class="outcomes">
      <li>Project Type: 2 Townhouse Development</li>
      <li>Total Project Costs: $1,900,000</li>
      <li>Total Cash/Equity Required: $627,991</li>
      <li>Indicative Project Net Profit: $250,093</li>
      <li>Indicative Project Return: 40%</li>
    </ul>
  </div>
  <p class="abs web proposal-web">www.<span>brightmeadowcollective</span>.com</p>
</section>

</body>
</html>
```